Banner Ad Design for beauty and personal care products Ad

Hi Designers,
We are need a beautiful banner ad design to be used in Trade Shows, Pinwheel, and to be displayed in Beauty Salon and spa. We supply pure, natural and 100% organic beauty and personal care products. We are headquartered in Boston USA
The design must be very attractive and inclusive. Our products are suitable for all skin types, therefore pictures must be race neural or inclusive or not be included at all.

Target Market(s)

Educated women, value buyers with mid to higher income level across all demographics ( white, black, Spanish and Asian).

Industry/Entity Type

Cosmetics

Font styles to use
Sans Serif

Colors

Designer to choose colors to be used in the design.

Requirements
Must have
• The banner needs to convey and include the following:
• 1- The categories of beauty and personal care products we sell
• 2- The fact that our products are pure, all-natural and 100% organic
• 3- Few of the key benefits from at least Hair and skin care, facial and body and bath categories that most women are likely to find appealing
• 4- An urgent call to action ( for example buy now)
• 5- How to contact us
Nice to have
• Pictures from each of the main product categories, call to actions and contact info.

```html
<!DOCTYPE html>
<html lang="en">
<head>
<meta charset="UTF-8">
<title>Essential Beauty Banner</title>
<link href="https://fonts.googleapis.com/css2?family=Montserrat:wght@400;500;600;700;800&display=swap" rel="stylesheet">
<style>
  :root {
    --orange: #f07f3a;
    --panel: #f3f3f3;
    --ink: #464646;
    --ink-soft: #555555;
    --teal: #a3cfcf;
    --white: #ffffff;
    --skin-light: #f3ddd2;
    --skin-mid: #e3bfae;
    --table: #ebe9e8;
  }
  * { margin: 0; padding: 0; box-sizing: border-box; }
  html, body { width: 1200px; height: 900px; overflow: hidden; background: var(--panel); }
  body { font-family: 'Montserrat', sans-serif; color: var(--ink); }
  .banner { position: relative; width: 1200px; height: 900px; background: var(--panel); overflow: hidden; }

  .hands-photo {
    position: absolute; left: 0; top: 0; width: 465px; height: 900px;
    background: linear-gradient(160deg, #e7eef2 0%, var(--skin-light) 30%, var(--skin-mid) 55%, var(--skin-light) 75%, var(--table) 100%);
  }
  .brand-title {
    position: absolute; left: 65px; top: 128px;
    color: var(--white); font-weight: 700; font-size: 53px; line-height: 1.0; letter-spacing: 2px;
  }
  .category-list { position: absolute; left: 66px; top: 320px; list-style: none; }
  .category-list li {
    color: var(--white); font-size: 22px; font-weight: 500; letter-spacing: 1.2px;
    line-height: 45.7px;
  }

  .headline {
    position: absolute; left: 527px; top: 124px;
    color: var(--orange); font-weight: 800; font-size: 47px; letter-spacing: -0.5px;
  }
  .subhead {
    position: absolute; left: 528px; top: 191px;
    font-size: 19.5px; font-weight: 500; letter-spacing: 1.2px; color: var(--ink);
  }
  .intro {
    position: absolute; left: 528px; top: 235px; width: 610px;
    font-size: 20px; line-height: 30.5px; letter-spacing: 0.6px; color: var(--ink-soft);
  }
  .product-shot { position: absolute; top: 404px; height: 176px; border-radius: 6px; }
  .product-carrot { left: 545px; width: 190px; background: linear-gradient(180deg, #b9a9a6 0%, #c9b7b2 55%, #f08a34 100%); }
  .product-clay { left: 766px; width: 190px; background: linear-gradient(180deg, #a69c9c 0%, #bdb0ae 55%, #c8573a 100%); }
  .product-spray { left: 980px; width: 150px; background: linear-gradient(180deg, #5a5572 0%, #8c7f8e 60%, #c2424a 100%); }

  .benefits {
    position: absolute; left: 525px; top: 611px;
    font-size: 20.5px; letter-spacing: 0.6px; color: var(--ink-soft); white-space: nowrap;
  }
  .benefits span { margin-left: 30px; font-size: 19px; }

  .accent-band { position: absolute; left: 0; top: 684px; width: 1200px; height: 17px; background: var(--orange); }

  .logo-name {
    position: absolute; left: 160px; top: 782px; display: flex; align-items: center; gap: 12px;
    color: var(--orange); font-weight: 700; font-size: 34px;
  }
  .logo-name i { display: block; width: 28px; height: 28px; border-radius: 50%; background: var(--orange); }

  .shop-button {
    position: absolute; left: 700px; top: 738px; width: 247px; height: 55px;
    background: var(--teal); color: var(--white); font-size: 19px; font-weight: 600; letter-spacing: 1px;
    display: flex; align-items: center; justify-content: center; text-decoration: none;
  }
  .contact {
    position: absolute; left: 524px; width: 600px; top: 810px; text-align: center;
    color: var(--orange); font-weight: 600; font-size: 20px; letter-spacing: 1px; line-height: 30.5px;
  }
</style>
</head>
<body>
<main class="banner">
  <div class="hands-photo" role="img" aria-label="Close-up of hands applying a dab of white cream"></div>
  <h1 class="brand-title">Essential<br>Beauty</h1>
  <ul class="category-list">
    <li>HAIR PRODUCTS</li>
    <li>BATH PRODUCTS</li>
    <li>SKIN CARE</li>
    <li>FACIAL REJUVINATION</li>
  </ul>

  <h2 class="headline">Beauty from nature.</h2>
  <p class="subhead">100% ORGANIC, ALL NATURAL INGREDIENTS.</p>
  <p class="intro">Choosing organic skincare products is a natural and effective way to get your skin feeling and looking radiant. Organic and natural products work with your skin to enhance its regenerative and healing properties.</p>

  <div class="product-shot product-carrot" role="img" aria-label="Jar of black soap with fresh carrots"></div>
  <div class="product-shot product-clay" role="img" aria-label="Jar of black soap with red clay powder"></div>
  <div class="product-shot product-spray" role="img" aria-label="Spray bottle with red berries and leaves"></div>

  <p class="benefits">Key benefits include:<span>Glowing skin, soft hair, pure care</span></p>

  <div class="accent-band"></div>

  <div class="logo-name"><i></i>Lumena</div>

  <a class="shop-button" href="#">SHOP NOW</a>
  <p class="contact">OR CONTACT US AT: WWW.LUMENA.COM<br>TO DISCOVER OUR RANGE</p>
</main>
</body>
</html>
```